Thai Takeaway Menu Design

I need a menu re-design for a thai takeaway/restaurant in australia.

Please use content from the existing menu
http://www.platterwink.example/u/menu/7302918?p=1

I'd like to emphasise on
1 - free delivery for order over $40
2 - gluten free and vegetatian option available on most meal (however you want to word it - not fuss)

*remove (the banner order online and save $10)

I'm happy to change the whole concept & design. I particularly like rustic, raw look more than moden ones. Does not need to be flowery or anything like current one :)

Industry/Entity Type

Restaurant

```html
<!DOCTYPE html>
<html lang="en">
<head>
<meta charset="utf-8">
<title>Baan Krua – Traditional Thai Cuisine Menu</title>
<link rel="stylesheet" href="https://fonts.googleapis.com/css2?family=Open+Sans:wght@400;600;700&display=swap">
<style>
  :root{
    --page:#ffffff;
    --gold:#f2a81d;
    --cream:#f6ecd8;
    --white:#ffffff;
    --red:#e0151b;
    --green:#1f8d2c;
  }
  *{margin:0;padding:0;box-sizing:border-box}
  html,body{width:1200px;height:900px;overflow:hidden;background:var(--page)}
  body{position:relative;font-family:"Open Sans",Arial,sans-serif;color:var(--white)}
  .panel{position:absolute;left:330px;width:554px;height:392px;overflow:hidden}
  .panel--cover{top:57px}
  .panel--menu{top:453px}
  .texture{position:absolute;inset:0}
  .panel--cover .texture{
    background:
      radial-gradient(ellipse at 20% 30%, rgba(196,140,50,.75), transparent 55%),
      radial-gradient(ellipse at 85% 90%, rgba(30,18,8,.9), transparent 60%),
      linear-gradient(135deg,#a8621f 0%,#8a4b1c 40%,#6a3a14 70%,#2e1c0c 100%);
  }
  .panel--menu .texture{
    background:
      radial-gradient(ellipse at 80% 25%, rgba(214,140,50,.8), transparent 55%),
      radial-gradient(ellipse at 15% 70%, rgba(20,14,6,.9), transparent 60%),
      linear-gradient(160deg,#5a4416 0%,#3a2a10 35%,#2a1c0c 60%,#8a5a22 100%);
  }
  .frames{position:absolute;inset:0}
  .deal{position:absolute;text-align:center;width:126px;font-size:7px;line-height:9.4px;color:var(--cream)}
  .deal h2{font-size:13px;font-weight:700;line-height:15px;color:var(--white);white-space:nowrap}
  .deal .price{font-size:16px;font-weight:700;line-height:19px;color:var(--white);margin-bottom:5px}
  .deal .note{margin-top:6px;font-size:6.5px;font-weight:600}
  .deal--dinner{left:22px;top:66px;width:146px}
  .deal--lunch{left:178px;top:131px;width:140px}
  .deal--family{left:25px;top:230px;width:146px}
  .brand{position:absolute;left:350px;top:62px;width:190px;text-align:center}
  .brand__name{font-size:30px;font-weight:600;color:var(--white);line-height:36px;white-space:nowrap}
  .brand__tag{font-size:9px;color:var(--white);letter-spacing:.5px}
  .brand__dot{display:inline-block;width:10px;height:10px;border-radius:50%;background:var(--white);margin-right:8px;vertical-align:middle}
  .services{position:absolute;left:345px;width:200px;top:172px;text-align:center;font-size:11px;font-weight:700;white-space:nowrap}
  .hours{position:absolute;left:335px;width:220px;top:193px;text-align:center;font-size:8.5px;line-height:12px;color:var(--gold)}
  .contact{position:absolute;left:363px;top:309px;font-size:9px;font-weight:700;line-height:12.5px;font-style:normal}
  .badge{position:absolute;border-radius:50%;display:flex;flex-direction:column;align-items:center;justify-content:center;text-align:center;color:var(--white)}
  .badge--free{left:481px;top:245px;width:58px;height:58px;background:var(--red);font-size:5.5px;font-weight:600;line-height:7px}
  .badge--free strong{font-size:13px;line-height:14px}
  .badge--diet{left:484px;top:311px;width:56px;height:56px;background:var(--green);font-size:5.5px;font-weight:600;line-height:7.5px;padding:0 6px}
  .column{position:absolute;top:26px;width:124px}
  .column--one{left:26px}
  .column--two{left:194px;top:30px;width:142px}
  .column--three{left:366px;top:33px;width:144px}
  .section{margin-bottom:11px}
  .section h3{font-size:12px;font-weight:700;color:var(--gold);line-height:15px}
  .item{display:flex;justify-content:space-between;gap:6px;font-size:7px;line-height:9.6px;color:var(--cream);white-space:nowrap}
  .veg{color:var(--gold)}
  .footnote{position:absolute;left:26px;top:360px;font-size:8px;font-weight:700}
  .footnote .veg{font-size:9px}
  .brand--small{left:428px;top:328px;width:116px}
  .brand--small .brand__name{font-size:20px;line-height:24px}
  .brand--small .brand__tag{font-size:7px}
</style>
</head>
<body>
  <section class="panel panel--cover">
    <div class="texture" role="img" aria-label="Rustic textured background with a traditional Thai temple carving in ochre and rust tones"></div>
    <svg class="frames" width="554" height="392" viewBox="0 0 554 392" aria-hidden="true">
      <g fill="none" stroke="#f6ecd8" stroke-width="1">
        <path d="M30 58 Q45 48 60 50 Q80 40 88 44 Q96 40 116 50 Q131 48 146 58 Q140 100 146 142 Q128 150 116 162 Q100 170 88 186 Q76 170 60 162 Q48 150 30 142 Q36 100 30 58Z"/>
        <path d="M188 108 Q203 98 218 100 Q238 90 247 94 Q256 90 276 100 Q291 98 306 108 Q300 160 306 212 Q288 220 276 232 Q260 240 247 256 Q234 240 218 232 Q206 220 188 212 Q194 160 188 108Z"/>
        <path d="M38 223 Q53 213 68 215 Q88 205 97 209 Q106 205 126 215 Q141 213 156 223 Q150 265 156 307 Q138 315 126 327 Q110 335 97 351 Q84 335 68 327 Q56 315 38 307 Q44 265 38 223Z"/>
      </g>
    </svg>
    <div class="deal deal--dinner">
      <h2>Dinner for Two</h2>
      <p class="price">$28</p>
      <p>Spring Rolls</p><p>Chicken and Cashew Nuts</p><p>Massaman Curry</p><p>Rice</p>
    </div>
    <div class="deal deal--lunch">
      <h2>Lunch Special</h2>
      <p class="price">$10</p>
      <p>Pad Thai</p><p>Sweet and Sour Pork /w Rice</p><p>Chicken and Cashew Nuts / w Rice</p><p>Green Curry Chicken /w Rice</p><p>Beef Noodle Soup</p>
      <p class="note">*FREE CAN OF SOFT DRINK*</p>
    </div>
    <div class="deal deal--family">
      <h2>Family Pack</h2>
      <p class="price">$45</p>
      <p>Spring Rolls (4)</p><p>Satay Chicken (4)</p><p>Chicken and Cashew Nuts</p><p>Red Curry Beef</p><p>Pad Thai</p><p>Rice (Large)</p>
    </div>
    <div class="brand">
      <p class="brand__name"><span class="brand__dot"></span>Baan Krua</p>
      <p class="brand__tag">Traditional Thai Cuisine</p>
    </div>
    <p class="services">Dine in • Takeaway • Delivery</p>
    <div class="hours">
      <p>Trading Hours</p>
      <p>Lunch (Wednesday- Sunday) 11:00 - 2:30pm</p>
      <p>Dinner (7 days) 5:00 - 9:30pm</p>
    </div>
    <address class="contact">
      <p>72 Wattle Road</p><p>Hillcrest</p><p>Corner of Banksia St</p><p>and Wattle Rd</p><p>Telephone: 07 3555 0148</p>
    </address>
    <div class="badge badge--free"><strong>FREE</strong><span>Delivery for</span><span>orders over $40</span></div>
    <div class="badge badge--diet"><span>Gluten free and vegetarian options available</span></div>
  </section>

  <section class="panel panel--menu">
    <div class="texture" role="img" aria-label="Dark rustic textured background with faint Thai carving in gold and umber tones"></div>
    <div class="column column--one">
      <div class="section"><h3>Entree</h3>
        <p class="item"><span>Spring Rolls<span class="veg">*</span> (4)</span><span>$6.00</span></p>
        <p class="item"><span>Satay Chicken (4)</span><span>$6.00</span></p>
        <p class="item"><span>Fish Cakes (4)</span><span>$6.00</span></p>
        <p class="item"><span>Dim Sim (4)</span><span>$6.00</span></p>
        <p class="item"><span>Duck Rice Paper Rolls<span class="veg">*</span> (2)</span><span>$6.00</span></p>
        <p class="item"><span>Papaya Salad</span><span>$6.00</span></p>
        <p class="item"><span>Tofu /w Peanut Sauce</span><span>$6.00</span></p>
      </div>
      <div class="section"><h3>Soup</h3>
        <p class="item"><span>Tom Yum Prawn<span class="veg">*</span></span><span>$7.00</span></p>
        <p class="item"><span>Tom Kha Chicken<span class="veg">*</span></span><span>$7.00</span></p>
      </div>
      <div class="section"><h3>Curry</h3>
        <p class="item"><span>Green Curry Chicken<span class="veg">*</span></span><span>$12.90</span></p>
        <p class="item"><span>Panang Chicken<span class="veg">*</span></span><span>$12.90</span></p>
        <p class="item"><span>Red Curry Beef<span class="veg">*</span></span><span>$12.90</span></p>
        <p class="item"><span>Massaman Beef Curry</span><span>$12.90</span></p>
        <p class="item"><span>Red Duck Curry</span><span>$16.90</span></p>
        <p class="item"><span>Yellow Curry Chicken<span class="veg">*</span></span><span>$12.90</span></p>
        <p class="item"><span>Yellow Curry Prawn</span><span>$16.90</span></p>
      </div>
      <div class="section"><h3>Vegetable</h3>
        <p class="item"><span>Mixed Vegetables<span class="veg">*</span></span><span>$10.50</span></p>
        <p class="item"><span>Steamed Veg /w Peanut Sauce<span class="veg">*</span></span><span>$10.50</span></p>
      </div>
      <div class="section"><h3>Beef</h3>
        <p class="item"><span>Beef /w Oyster Sauce<span class="veg">*</span></span><span>$12.90</span></p>
        <p class="item"><span>Grilled Beef Salad<span class="veg">*</span></span><span>$12.90</span></p>
      </div>
    </div>
    <div class="column column--two">
      <div class="section"><h3>Chicken</h3>
        <p class="item"><span>Laab Chicken<span class="veg">*</span></span><span>$12.90</span></p>
        <p class="item"><span>Chicken w/ Sweet Basil<span class="veg">*</span></span><span>$12.90</span></p>
        <p class="item"><span>Chicken w/ Cashew Nuts</span><span>$12.90</span></p>
        <p class="item"><span>Grilled Chicken w/ Salad</span><span>$12.90</span></p>
        <p class="item"><span>Southern Style Fried Chicken</span><span>$12.90</span></p>
      </div>
      <div class="section"><h3>Pork</h3>
        <p class="item"><span>Sweet and Sour Pork<span class="veg">*</span></span><span>$12.90</span></p>
        <p class="item"><span>Garlic Pork</span><span>$12.90</span></p>
        <p class="item"><span>Crispy Pork w/ Asian Greens<span class="veg">*</span></span><span>$12.90</span></p>
      </div>
      <div class="section"><h3>Duck</h3>
        <p class="item"><span>Roast Duck /w Vegetable and Gravy</span><span>$16.90</span></p>
        <p class="item"><span>Duck /w Sweet Basil</span><span>$16.90</span></p>
        <p class="item"><span>Honey Glazed Duck /w Vegetable</span><span>$16.90</span></p>
      </div>
      <div class="section"><h3>Seafood</h3>
        <p class="item"><span>Garlic Prawn</span><span>$16.90</span></p>
        <p class="item"><span>Tamarind Prawn</span><span>$16.90</span></p>
        <p class="item"><span>Laab Fish</span><span>$16.90</span></p>
        <p class="item"><span>Crispy Fish /w Sweet Chilli Salsa</span><span>$16.90</span></p>
        <p class="item"><span>Chilli and Lime Calamari Salad</span><span>$16.90</span></p>
        <p class="item"><span>Salt and Pepper Calamari</span><span>$16.90</span></p>
        <p class="item"><span>Spicy Seafood</span><span>$16.90</span></p>
        <p class="item"><span>Crispy Barramundi /w Green</span><span></span></p>
        <p class="item"><span>Mango Salad (Seasonal)</span><span>$22.90</span></p>
        <p class="item"><span>Soft Shell Chilli Crab</span><span>$22.90</span></p>
      </div>
    </div>
    <div class="column column--three">
      <div class="section"><h3>Noodle</h3>
        <p class="item"><span>Pad Thai<span class="veg">*</span></span><span>$12.50</span></p>
        <p class="item"><span>Pad Thai Prawn</span><span>$16.90</span></p>
        <p class="item"><span>Drunken Noodle<span class="veg">*</span></span><span>$12.50</span></p>
        <p class="item"><span>Pad See Eew<span class="veg">*</span></span><span>$12.50</span></p>
        <p class="item"><span>Beef Noodle Soup</span><span>$12.50</span></p>
        <p class="item"><span>Seafood Laksa</span><span>$16.90</span></p>
      </div>
      <div class="section"><h3>Rice</h3>
        <p class="item"><span>Rice (Small)</span><span>$2.50</span></p>
        <p class="item"><span>Rice (Large)</span><span>$3.50</span></p>
        <p class="item"><span>Coconut Rice (Small)</span><span>$4.50</span></p>
        <p class="item"><span>Coconut Rice (Large)</span><span>$5.50</span></p>
        <p class="item"><span>Fried Rice</span><span>$10.50</span></p>
        <p class="item"><span>Roti Bread</span><span>$3.50</span></p>
      </div>
      <div class="section"><h3>Dessert</h3>
        <p class="item"><span>Black Sticky Rice /w Coconut Cream</span><span>$4.50</span></p>
        <p class="item"><span>Tapioca Pudding /w Lychee</span><span>$4.50</span></p>
      </div>
      <div class="section"><h3>Drinks</h3>
        <p class="item"><span>Kola, Diet Kola, Orango, Limeade</span><span></span></p>
        <p class="item"><span>(Zesto 375ml)</span><span>$2.00</span></p>
        <p class="item"><span>Kola, Orango, Limeade (1.25L)</span><span>$4.50</span></p>
        <p class="item"><span>Orange Juice/Apple Juice</span><span>$3.50</span></p>
        <p class="item"><span>Ginger Beer</span><span>$3.50</span></p>
      </div>
    </div>
    <p class="footnote"><span class="veg">*</span>Available as vegetarian on request</p>
    <div class="brand brand--small">
      <p class="brand__name">Baan Krua</p>
      <p class="brand__tag">Traditional Thai Cuisine</p>
    </div>
  </section>
</body>
</html>
```